Brochure Design - ICT Company

We are an ICT (Information & Communication Technologies) company and need a brochure design. Our main products and services are Office Equipment, Banking Equipment, Software Solutions, IT Hardware, Networking & Communication, Audio Video Solutions and Social Media Marketing. Please check our website www.dalvorinex.com for details in our Solutions menu.

Designs should include colors from our website (blue) and our logo (orange/green) in the best possible combination with lighter colors. Graphics and patterns should be sleek and modern. Brochure size to be square shaped (21 cm x 21 cm).

Final design should portray us as a futuristic technology company.

Provide a design with sample images and we can purchase them if required. Alternatively, let us know if the images from our website will suffice.
Updates

Project Deadline Extended
Reason: Awaiting more designs and more creativity. If any input is required from us, do inform asap.

Uploaded 2 sample brochure designs that we found interesting - looking for more inspiring ideas.

Thanks

Hi everyone, the following text should appear on the cover of the brochure design:

'Your One Stop Solution Provider for Information & Communication Technologies'

Project Deadline Extended
Reason: Awaiting management feedback - might require changes in design. Open to receiving more designs.

Thank you all for participating. Received many creative ideas and will be back with more requests. 

Target Market(s)

Decision Makers in UAE: IT Managers, Purchase Manager, CEO, Finance Managers etc

Industry/Entity Type

Communication

Requirements
Must have
• We have 7 divisions within our company. Brochure should dedicate 2 pages to each company - Text on one side and Image on the other.

7 divisions are: (details on website)
Office Equipment - sales of copiers, fax etc to any industry, any size office
Banking Equipment - sales of coin counters, counterfeit detectors etc to banks and foreign exchange houses
IT & Communication - providing server, email, software licenses to any industry, any size office
Software Solution - Quillon partner + provide software solution to any industry, any size company
ELV & Security - provide CCTV, security systems to big companies, warehouses etc any industry
AV & Convergence - provide latest technology multi sensory solutions for theatres, opera houses, education sector, hospitality sector, medical sector etc.
Social Media Marketing - provide marketing options to companies through social media (www.dalvoripost.com)

Images to be used in the brochure are attached - they are concept images associated with each division. The design for the inner pages can be created around this basic image.

Cover page - design with logo, 'An Information & Technologies Company'
Back page - Design with address details
Inner sections:
1. About Us
2. Seven divisions as described above

The pattern for the text for inner pages should be:
Heading describing problem
Small Paragraph text describing solution
Small inset images of the

Nice to have
• Modern, sleek look with images that reflect an ICT/IT company - stand out from the regular brochure design
Should not have
• The design should not use old-style design, fonts etc.

```html
<!DOCTYPE html>
<html lang="en">
<head>
<meta charset="utf-8">
<title>ELV &amp; Security – Dalvorinex Technologies</title>
<link href="https://fonts.googleapis.com/css2?family=Baumans&family=Oswald:wght@500;600&family=Signika:wght@400;600&display=swap" rel="stylesheet">
<style>
  :root{
    --backdrop:#000000;
    --paper:#ffffff;
    --navy:#143a62;
    --orange:#e2701f;
    --ink:#1d1d1d;
    --muted:#555b63;
    --rule:#b9bfc6;
    --blue-deep:#0b3f8f;
    --blue-mid:#1466c2;
    --blue-bright:#2aa6e8;
    --card-dark:#1c2a52;
    --lime:#8cc63f;
  }
  *{margin:0;padding:0;box-sizing:border-box}
  html,body{width:1200px;height:900px;overflow:hidden;background:var(--backdrop)}
  .spread{position:absolute;left:38px;top:171px;width:1120px;height:560px;background:var(--paper)}
  .section-title{position:absolute;left:40px;top:32px;font-family:"Baumans",sans-serif;font-size:43px;color:var(--navy);letter-spacing:.5px;line-height:1}
  .tagline{position:absolute;left:40px;top:80px;font-family:"Baumans",sans-serif;font-size:20px;line-height:24px;color:var(--orange)}
  .solutions{position:absolute;right:943px;top:147px;text-align:right;font-family:"Signika",sans-serif;font-size:12.5px;line-height:16px;color:var(--ink)}
  .solutions h3{font-family:"Oswald",sans-serif;font-weight:600;font-size:11.5px;color:var(--navy);letter-spacing:.3px;margin-bottom:1px}
  .solutions li{list-style:none;margin-right:-16px;padding-right:16px;position:relative}
  .solutions li + li{margin-top:0}
  .solutions .bullet{position:absolute;right:0;top:3px;width:10px;height:10px}
  .body-copy{position:absolute;left:193px;top:145px;width:322px;font-family:"Signika",sans-serif;font-size:12.5px;line-height:17px;color:var(--ink)}
  .body-copy p + p{margin-top:10px}
  .drop-cap{float:left;font-size:38px;line-height:30px;margin:2px 3px 0 0;color:var(--ink)}
  .equipment{position:absolute;left:194px;top:376px;width:156px;border-collapse:collapse;font-family:"Signika",sans-serif;font-size:10px;color:var(--ink)}
  .equipment th{background:var(--navy);color:#fff;text-align:left;font-weight:600;padding:2px 3px;height:15px}
  .equipment td{border:1px solid var(--rule);padding:1px 3px;height:15px}
  .page-marker{position:absolute;left:0;top:489px;width:8px;height:31px;background:var(--navy)}
  .page-number{position:absolute;left:22px;top:482px;font-family:"Oswald",sans-serif;font-weight:500;font-size:38px;line-height:1;color:var(--muted)}
  .company{position:absolute;left:22px;top:522px;font-family:"Signika",sans-serif;font-size:8px;line-height:9px;color:var(--muted)}
  .visual{position:absolute;left:574px;top:14px;width:533px;height:532px;border-radius:10px;overflow:hidden;
    background:radial-gradient(circle at 50% 40%,var(--blue-bright) 0%,var(--blue-mid) 45%,var(--blue-deep) 100%)}
  .visual .card{position:absolute;left:97px;top:113px;width:342px;height:236px;border-radius:14px;
    background:radial-gradient(circle at 40% 45%,#4b8fd6 0%,#2a4b8c 40%,var(--card-dark) 100%)}
  .visual .band{position:absolute;left:97px;top:224px;width:342px;height:22px;background:var(--lime);opacity:.85}
</style>
</head>
<body>
<main class="spread">
  <h1 class="section-title">ELV &amp; SECURITY</h1>
  <h2 class="tagline">AT EVERY CHECK POINT,<br>WE ARE THERE</h2>

  <ul class="solutions">
    <h3>OUR SOLUTIONS</h3>
    <li>Provide CCTV<svg class="bullet" viewBox="0 0 10 10"><circle cx="5" cy="5" r="5" fill="#8a8f96"/><path d="M6 2.5 3.5 5 6 7.5" stroke="#fff" stroke-width="1.4" fill="none"/></svg></li>
    <li>Security systems<svg class="bullet" viewBox="0 0 10 10"><circle cx="5" cy="5" r="5" fill="#8a8f96"/><path d="M6 2.5 3.5 5 6 7.5" stroke="#fff" stroke-width="1.4" fill="none"/></svg></li>
    <li style="padding-right:0;margin-right:0">to big companies</li>
    <li>Warehouses etc<svg class="bullet" viewBox="0 0 10 10"><circle cx="5" cy="5" r="5" fill="#8a8f96"/><path d="M6 2.5 3.5 5 6 7.5" stroke="#fff" stroke-width="1.4" fill="none"/></svg></li>
    <li style="padding-right:0;margin-right:0">any industry</li>
  </ul>

  <div class="body-copy">
    <p><span class="drop-cap">O</span>ur security services are suitable for a wide range of requirements from domestic to commercial applications and serving government and public sector contracts. These days, cameras and other video equipment have become an integral part of the security systems.</p>
    <p>We offer you total Security &amp; Surveillance Solutions - CCTV &amp; Video Monitoring, Displays and Alarm Systems, Access Control and Time attendance Systems, Gate Barriers, , Control Centralized Monitoring Systems, Explosive Detection Systems, Baggage Scanners, Video Intercom(Indoor &amp; Outdoor) Fire Alarm systems, Fire Telephones &amp; Evacuation Systems</p>
  </div>

  <table class="equipment">
    <tr><th>EQUIPMENT</th></tr>
    <tr><td>CCTV</td></tr>
    <tr><td>Access Control</td></tr>
    <tr><td>Garage Doors</td></tr>
  </table>

  <div class="page-marker"></div>
  <div class="page-number">12</div>
  <div class="company">DALVORINEX<br>TECHNOLOGIES LLC</div>

  <div class="visual" role="img" aria-label="Illustration of a security access card with a fingerprint and green security band over a blue tiled pattern">
    <div class="card"></div>
    <div class="band"></div>
  </div>
</main>
</body>
</html>
```